Cool blackchain based app company needs a website :)

pillcheckhub.net

Kinda says it all!! This is an app which sits on your smartfone / tablet. You scan a QR code from a medicinal product and our app will verify if the product you have is genuine. It's simple, It's free.

The design could be very modern and simple. It should show in graphical form how the app works and have FAQ's etc.

pillcheckhub.net is designed specifically to allow consumers verify that the medical products which they have purchased are genuine.

Detailed brief with content attached. Logo in high res and QR code attached.

Full website required.
Updates

Target Market(s)

Pharmaceutical

Industry/Entity Type

Pharmaceutical

Coding

Coded - Design and coding required

Number of Pages Required

3 page

Colors

Designer to choose colors to be used in the design.

Requirements
Must have
• Strong visuals - very simple navigation - 3 pages
Nice to have
• Animation of the process
Should not have
• Jargon!

```html
<!DOCTYPE html>
<html lang="en">
<head>
<meta charset="utf-8">
<title>About Us – pillcheckhub.net</title>
<link rel="stylesheet" href="https://fonts.googleapis.com/css2?family=Montserrat:wght@300;400;500;600;700&display=swap">
<style>
  :root {
    --brand-blue: #1f6db3;
    --brand-navy: #1d4f8c;
    --brand-green: #5aa53a;
    --text-grey: #5a5a5a;
    --heading-grey: #4e4e4e;
    --nav-grey: #6a6a6a;
    --photo-warm: #8a7468;
    --photo-cool: #c9c9c9;
    --page-bg: #ffffff;
  }
  * { margin: 0; padding: 0; box-sizing: border-box; }
  html, body { width: 1074px; height: 1200px; overflow: hidden; background: var(--page-bg); }
  body { font-family: "Montserrat", sans-serif; color: var(--text-grey); position: relative; }

  .site-header { position: absolute; top: 0; left: 0; width: 1074px; height: 130px; }
  .main-nav { position: absolute; left: 155px; top: 96px; font-size: 9px; color: var(--nav-grey); display: flex; gap: 13px; }
  .main-nav a { color: inherit; text-decoration: none; }
  .main-nav .current { color: var(--brand-blue); font-weight: 600; }
  .brand { position: absolute; left: 0; width: 1074px; text-align: center; }
  .brand-header { top: 20px; }
  .brand-mark { display: block; margin: 0 auto; border-radius: 50%; background: var(--brand-green); }
  .brand-header .brand-mark { width: 54px; height: 54px; margin-bottom: 14px; }
  .brand-name { font-weight: 700; color: var(--brand-navy); }
  .brand-header .brand-name { font-size: 16px; }
  .contact { position: absolute; right: 154px; top: 95px; display: flex; align-items: center; gap: 9px; font-size: 8px; font-weight: 600; color: var(--brand-blue); }
  .contact .divider { color: var(--heading-grey); font-size: 11px; }

  .section-title { position: absolute; left: 0; width: 1074px; text-align: center; font-weight: 700; color: var(--brand-blue); font-size: 25px; }
  .about-title { top: 148px; }
  .founders-title { top: 468px; }

  .about-copy { position: absolute; left: 207px; top: 206px; width: 660px; text-align: center; font-size: 14.5px; font-weight: 300; line-height: 19.4px; }
  .about-copy p { margin-bottom: 19.4px; }
  .about-copy strong { color: var(--brand-blue); font-weight: 600; }

  .founder { position: absolute; }
  .founder-name { font-size: 14px; font-weight: 600; color: var(--heading-grey); margin-bottom: 18px; letter-spacing: 0.2px; }
  .founder-bio { font-size: 14.5px; font-weight: 300; line-height: 19.4px; }
  .founder-ceo { left: 150px; top: 550px; width: 374px; text-align: right; }
  .founder-cio { left: 550px; top: 756px; width: 370px; }
  .portrait { position: absolute; display: block; }
  .portrait-ceo { left: 552px; top: 555px; width: 145px; height: 146px; background: linear-gradient(160deg, #5b5552, var(--photo-warm) 55%, #3a3a40); }
  .portrait-cio { left: 408px; top: 760px; width: 115px; height: 149px; background: linear-gradient(180deg, #f1f1f1, var(--photo-cool) 55%, #2a2a2e); }

  .site-footer { position: absolute; left: 0; top: 996px; width: 1074px; }
  .brand-footer { top: 0; }
  .brand-footer .brand-mark { width: 88px; height: 88px; margin-bottom: 14px; }
  .brand-footer .brand-name { font-size: 22px; }
  .footer-nav { position: absolute; top: 139px; left: 0; width: 1074px; display: flex; justify-content: center; gap: 14px; font-size: 9px; color: var(--nav-grey); }
  .footer-nav a { color: inherit; text-decoration: none; }
  .legal { position: absolute; top: 161px; left: 0; width: 1074px; text-align: center; font-size: 8.5px; color: var(--nav-grey); }
  .legal .builder { color: var(--brand-green); font-weight: 600; }
  .legal .sep { margin: 0 9px; }
</style>
</head>
<body>
  <header class="site-header">
    <nav class="main-nav">
      <a href="#">Home</a><span>I</span>
      <a href="#">FAQ</a><span>I</span>
      <a href="#" class="current">About Us</a>
    </nav>
    <div class="brand brand-header">
      <span class="brand-mark"></span>
      <span class="brand-name">pillcheckhub.net</span>
    </div>
    <div class="contact">
      <svg width="6" height="12" viewBox="0 0 6 12" aria-hidden="true"><path d="M5 0.5 C1.5 1.5 0.5 4 0.5 6 C0.5 8 1.5 10.5 5 11.5 L5.5 9 C3.5 8.5 3 7.5 3 6 C3 4.5 3.5 3.5 5.5 3 Z" fill="currentColor"/></svg>
      <span>+353 87 555 0192</span>
      <span class="divider">|</span>
      <svg width="15" height="11" viewBox="0 0 15 11" aria-hidden="true"><rect x="0" y="0" width="15" height="11" fill="currentColor"/><path d="M0.5 0.5 L7.5 6 L14.5 0.5 M0.5 10.5 L5.5 5 M14.5 10.5 L9.5 5" stroke="#fff" stroke-width="1.2" fill="none"/></svg>
    </div>
  </header>

  <h1 class="section-title about-title">About</h1>
  <section class="about-copy">
    <p>Founded by two long time and highly experienced friends, Daniel Whitcombe and Marcus Delaney, pillcheckhub is dedicated to reducing the number of people who suffer due to counterfeit medical products.</p>
    <p>The pharmaceutical industry is leading the way in terms of investing in anti-counterfeiting solutions to protect consumers.&nbsp; However, counterfeit medicine is a huge business, estimated to be worth over <strong>€100 billion</strong> annually.</p>
    <p>Using their combined knowledge and experience in the data security and anti-fraud industries, Daniel and Marcus have developed a (patent pending) highly secure, fast and free solution to protecting people against counterfeit medicines.</p>
  </section>

  <h2 class="section-title founders-title">The Founders</h2>

  <article class="founder founder-ceo">
    <h3 class="founder-name">Daniel Whitcombe, CEO</h3>
    <p class="founder-bio">Daniel is a global business leader who has been on the founding team of a number of software companies, leading with patented solutions. Daniel has a proven reputation and ability to ‘start from scratch’ in new markets, developing sales, marketing and delivery organisations.</p>
  </article>
  <div class="portrait portrait-ceo" role="img" aria-label="Portrait photo of Daniel Whitcombe, CEO"></div>

  <div class="portrait portrait-cio" role="img" aria-label="Portrait photo of Marcus Delaney, CIO"></div>
  <article class="founder founder-cio">
    <h3 class="founder-name">Marcus Delaney, CIO</h3>
    <p class="founder-bio">Marcus is a highly experienced technologist, innovator, visionary and entrepreneur specializing in Architectural and Network Security, Blockchain Deployments, Distributed Architecture and Cloud Computing. Marcus has over twenty-five years of</p>
  </article>

  <footer class="site-footer">
    <div class="brand brand-footer">
      <span class="brand-mark"></span>
      <span class="brand-name">pillcheckhub.net</span>
    </div>
    <nav class="footer-nav">
      <a href="#">Home</a><span>I</span>
      <a href="#">FAQ</a><span>I</span>
      <a href="#">About Us</a>
    </nav>
    <p class="legal">© 2016 Northvale. All rights reserved.<span class="sep">I</span>Built By <span class="builder">Brightform Studio</span></p>
  </footer>
</body>
</html>
```